Business Card Design For A Renovation Contractor Company

We need a business card for a new company based in Singapore, our company name is "KM Bravant". We are a renovation contractor that builds designs into reality. We build more of F&B restaurants, retail stores and commercial offices. We work very closely with designers. The final design should communicate to our client that we are a company that you can trust, that will plan and complete your project without giving you a headache. I like my client to remember my company as "KM". The beauty of SIMPLE is important.

Industry/Entity Type

Contractor

Requirements
Nice to have
• Black or Red base

```html
<!DOCTYPE html>
<html lang="en">
<head>
<meta charset="utf-8">
<title>KM Bravant — Business Card</title>
<link rel="stylesheet" href="https://fonts.googleapis.com/css2?family=Didact+Gothic&family=Open+Sans:wght@700&family=PT+Sans+Narrow&display=swap">
<style>
  :root {
    --bg: #e9e6e1;
    --black-top: #2a2a2a;
    --black-bottom: #0b0b0b;
    --red: #d8202a;
    --red-light: #ea3a44;
    --red-dark: #a8141c;
    --white: #ffffff;
    --grey: #d9d9d9;
    --pink: #f4b9bc;
    --tab-dark: #1a1a1a;
  }
  * { margin: 0; padding: 0; box-sizing: border-box; }
  html, body { width: 1200px; height: 1023px; overflow: hidden; }
  body {
    background: var(--bg);
    position: relative;
    font-family: "Didact Gothic", "Century Gothic", sans-serif;
  }
  .card {
    position: absolute;
    left: 215px;
    width: 770px;
    height: 440px;
    border-radius: 6px;
    overflow: hidden;
    box-shadow: 0 10px 24px rgba(0,0,0,.25);
  }
  .card--front {
    top: 45px;
    background: linear-gradient(160deg, var(--black-top), var(--black-bottom) 70%);
  }
  .card--back {
    top: 538px;
    background: radial-gradient(ellipse at 55% 45%, var(--red-light), var(--red) 55%, var(--red-dark));
  }
  .tab {
    position: absolute;
    width: 20px;
    height: 90px;
  }
  .card--front .tab { top: 40px; right: 0; border-radius: 6px 0 0 6px; background: var(--red); }
  .card--back .tab { bottom: 40px; left: 0; border-radius: 0 6px 6px 0; background: var(--tab-dark); }

  .brand { position: absolute; color: var(--white); }
  .brand__row { display: flex; align-items: center; gap: 14px; }
  .brand__dot {
    flex: none;
    width: 60px; height: 60px; border-radius: 50%;
    border: 5px solid var(--white);
  }
  .brand__name { font-size: 52px; line-height: 1; white-space: nowrap; }
  .brand__tagline {
    margin-top: 8px;
    padding-top: 4px;
    border-top: 2px solid var(--grey);
    font-size: 20px;
    color: var(--grey);
    white-space: nowrap;
  }
  .card--front .brand { left: 50px; top: 255px; }
  .card--back .brand { left: 190px; top: 145px; }

  .contact {
    position: absolute;
    left: 470px;
    top: 70px;
    color: var(--white);
  }
  .contact__name { font-family: "Open Sans", Arial, sans-serif; font-weight: 700; font-size: 30px; }
  .contact__role { font-family: Georgia, serif; font-weight: 700; color: var(--red); font-size: 17px; margin-bottom: 34px; }
  .contact__address, .contact__lines {
    font-family: "PT Sans Narrow", "Arial Narrow", sans-serif;
    font-style: normal;
    font-size: 19px;
    line-height: 1.3;
    list-style: none;
  }
  .contact__lines { margin-top: 20px; }
  .contact__lines li { display: flex; align-items: center; gap: 10px; }
  .contact__lines svg { width: 14px; height: 14px; fill: var(--red); }

  .web {
    position: absolute;
    left: 445px; top: 330px;
    color: var(--pink);
    font-size: 22px;
  }
</style>
</head>
<body>
  <section class="card card--front" aria-label="Card front">
    <div class="tab"></div>
    <div class="brand">
      <div class="brand__row">
        <span class="brand__dot"></span>
        <span class="brand__name">KM Bravant</span>
      </div>
      <div class="brand__tagline">turning plans into spaces</div>
    </div>
    <div class="contact">
      <div class="contact__name">Marcus Tan</div>
      <div class="contact__role">Director</div>
      <address class="contact__address">
        8 Keong Saik Lane<br>
        #03-210 Keong Saik Court<br>
        Singapore 089125
      </address>
      <ul class="contact__lines">
        <li><svg viewBox="0 0 16 16"><path d="M3 1l3 3-2 2c1 2 3 4 5 5l2-2 3 3-2 3C6 15 1 10 1 3z"/></svg>555-014-2288</li>
        <li><svg viewBox="0 0 16 16"><path d="M4 1h6v4H4zM1 6h14v7H1zM4 10h8v5H4z"/></svg>555-014-2289</li>
        <li><svg viewBox="0 0 16 16"><path d="M1 3h14v10H1zM2 4l6 5 6-5v1L8 10 2 5z" fill-rule="evenodd"/></svg>marcus@kmbravant.com</li>
      </ul>
    </div>
  </section>

  <section class="card card--back" aria-label="Card back">
    <div class="tab"></div>
    <div class="brand">
      <div class="brand__row">
        <span class="brand__dot"></span>
        <span class="brand__name">KM Bravant</span>
      </div>
      <div class="brand__tagline">turning plans into spaces</div>
    </div>
    <div class="web">www.kmbravant.com</div>
  </section>
</body>
</html>
```